Lock Company Van

The Ironwood Lock Company needs a design for the side and back of our service vans.
Updates

Target Market(s)

B2B, Retail Stores, Individual Customers

Industry/Entity Type

Locksmith

Requirements
Must have
• "Protect yourself with THE IRONWOOD" as a tagline.

```html
<!DOCTYPE html>
<html lang="en">
<head>
<meta charset="utf-8">
<title>The Ironwood Lock Company – Van Wrap</title>
<link rel="stylesheet" href="https://fonts.googleapis.com/css2?family=Oswald:wght@500;600;700&display=swap">
<style>
  :root {
    --canvas: #ffffff;
    --panel-light: #e9e9ea;
    --slate: #5b6571;
    --slate-dark: #4a525c;
    --brand-red: #ee2a35;
    --text-light: #ffffff;
  }
  * { margin: 0; padding: 0; box-sizing: border-box; }
  html, body { width: 1200px; height: 1200px; overflow: hidden; background: var(--canvas); }
  body { position: relative; font-family: "Oswald", "Arial Narrow", sans-serif; }

  .wrap-panel { position: absolute; overflow: hidden; border-radius: 18px; background: var(--panel-light); }
  .wrap-panel .band { position: absolute; inset: 0; width: 100%; height: 100%; }

  .brand { position: absolute; display: flex; align-items: center; gap: 14px; }
  .brand-mark { background: var(--brand-red); flex: none; }
  .brand-name { color: var(--brand-red); font-weight: 600; text-transform: uppercase; line-height: 1.05; white-space: nowrap; }
  .tagline { position: absolute; color: var(--slate-dark); font-weight: 500; letter-spacing: 0.5px; line-height: 1.2; }

  /* Side panel */
  .side { left: 40px; top: 60px; width: 1120px; height: 420px; }
  .side .brand { left: 450px; top: 70px; }
  .side .brand-mark { width: 40px; height: 40px; }
  .side .brand-name { font-size: 44px; letter-spacing: 1px; }
  .side .tagline { left: 504px; top: 132px; font-size: 20px; }

  .services { position: absolute; list-style: none; color: var(--text-light); font-weight: 500; line-height: 1.25; }
  .services li { position: relative; padding-left: 16px; }
  .services li::before { content: ""; position: absolute; left: 0; top: 0.55em; width: 7px; height: 7px; border-radius: 50%; background: currentColor; }
  .side .services { left: 480px; top: 222px; font-size: 19px; }

  .phone-main { position: absolute; font-weight: 700; letter-spacing: 1px; line-height: 1; }
  .side .phone-main { right: 70px; top: 222px; font-size: 44px; color: var(--text-light); }

  .web { position: absolute; font-weight: 700; color: var(--text-light); line-height: 1; letter-spacing: 1px; }
  .web em { font-style: normal; color: var(--brand-red); }
  .side .web { left: 300px; top: 332px; font-size: 56px; }

  /* Back panel */
  .back { left: 340px; top: 560px; width: 520px; height: 440px; }
  .back .brand { left: 28px; top: 36px; gap: 10px; flex-direction: column; align-items: flex-start; }
  .back .brand-mark { width: 30px; height: 30px; }
  .back .brand-name { font-size: 26px; }
  .back .tagline { left: 28px; top: 146px; width: 230px; font-size: 15px; }
  .back .services { left: 270px; top: 44px; font-size: 17px; color: var(--slate-dark); line-height: 1.2; }
  .back .services li { margin-bottom: 8px; }
  .back .phone-main { left: 0; right: 0; top: 196px; text-align: center; font-size: 42px; color: var(--slate); }
  .contact { position: absolute; left: 30px; top: 280px; list-style: none; color: var(--text-light); font-size: 20px; font-weight: 600; }
  .contact li { display: flex; align-items: center; gap: 10px; margin-bottom: 6px; }
  .contact svg { width: 22px; height: 22px; fill: none; stroke: currentColor; stroke-width: 2; }
  .back .web { left: 0; right: 0; top: 378px; text-align: center; font-size: 36px; }
</style>
</head>
<body>

<section class="wrap-panel side" aria-label="Van side wrap">
  <svg class="band" viewBox="0 0 1120 420" preserveAspectRatio="none" aria-hidden="true">
    <path d="M0 250 C 200 230, 450 200, 620 190 C 820 180, 1000 185, 1120 188 L1120 420 L0 420 Z" fill="var(--slate)"/>
  </svg>
  <div class="brand">
    <span class="brand-mark"></span>
    <span class="brand-name">The Ironwood Lock Company</span>
  </div>
  <p class="tagline">Protect yourself with THE IRONWOOD</p>
  <ul class="services">
    <li>Fast and professional<br>locksmith service</li>
    <li>24-hour service</li>
    <li>Years of experience</li>
  </ul>
  <p class="phone-main">(123)-456-7890</p>
  <p class="web">www.<em>website</em>.com</p>
</section>

<section class="wrap-panel back" aria-label="Van back wrap">
  <svg class="band" viewBox="0 0 520 440" preserveAspectRatio="none" aria-hidden="true">
    <path d="M0 258 Q 260 240 520 258 L520 440 L0 440 Z" fill="var(--slate)"/>
  </svg>
  <div class="brand">
    <span class="brand-mark"></span>
    <span class="brand-name">The Ironwood<br>Lock Company</span>
  </div>
  <p class="tagline">Protect yourself with THE IRONWOOD</p>
  <ul class="services">
    <li>Fast and professional<br>locksmith service</li>
    <li>24-hour service</li>
    <li>Years of experience</li>
  </ul>
  <p class="phone-main">(123)-456-7890</p>
  <ul class="contact">
    <li>
      <svg viewBox="0 0 24 24" aria-hidden="true"><rect x="6" y="2" width="12" height="20" rx="2"/><line x1="10" y1="18" x2="14" y2="18"/></svg>
      123-456-7890
    </li>
    <li>
      <svg viewBox="0 0 24 24" aria-hidden="true"><path d="M3 10 L12 3 L21 10 V20 H3 Z"/><path d="M3 10 L12 16 L21 10"/></svg>
      mail@mail.com
    </li>
  </ul>
  <p class="web">www.<em>website</em>.com</p>
</section>

</body>
</html>
```